Stationary for a Hand Therapy Clinic
Letterhead/banner, envelopes, business cards
Stationary for a Hand Therapy Clinic - Health
Creative Brief
Professional
Miriam Dorsey, OTD, OTR/L, CHT
Certified Hand Therapist
27548 52nd Ave W Ste 118 Lynnwood, WA 98036
miriam@palmrestcare.example
www.palmrestcare.example
I am open to ideas for placement of: Elbows - Wrists - Fingers (replace dashes with dots) and We guide each step toward fuller days.
We guide each step toward fuller days
miriamdorsey miriamdorsey
Windowed and standard envelopes both are appreciated too! Also, a half sheet sized folder is also great.
One additional item we will need is design for a name tag. Current ones are approximately 1x3" or 1.5x3.5" or so. Likely including the logo, employee's first name and title, such as Certified Hand Therapist, Occupational Therapist, Licensed OT Assistant, Operations Manager, and Patient Care Coordinator.
We definitely prefer orange over green as the primary color for the back side of the business cards and in stationary/other products.
Please use design from entry #439 in our logo contest, replacing dashes with dots. FONT: NEXA BOLD (Or your discretion; others possible) PRIMARY COLORS: ORANGE (#D18122) AND GREEN (#738F52) ACCENT COLORS: BROWN (#544741), LIGHT GREEN (#B9C4AC), RED #993B2C, OR BLUE (#538898) BLACK (#2F3334) WHITE (F0F1E8) PLEASE do not use logos/image from our current website. It will be updated with the new logo.

```html
<!DOCTYPE html>
<html lang="en">
<head>
<meta charset="utf-8">
<title>Name Tag – Miriam Dorsey</title>
<link rel="stylesheet" href="https://fonts.googleapis.com/css2?family=Questrial&display=swap">
<style>
  :root {
    --backdrop: #a9a8a8;
    --metal-light: #f2f2f2;
    --metal-mid: #dcdcdc;
    --metal-dark: #c6c6c6;
    --ink: #1a1a1a;
  }
  * { margin: 0; padding: 0; box-sizing: border-box; }
  html, body {
    width: 1200px;
    height: 720px;
    overflow: hidden;
    background: var(--backdrop);
  }
  .canvas {
    position: relative;
    width: 1200px;
    height: 720px;
  }
  .name-tag {
    position: absolute;
    left: 144px;
    top: 156px;
    width: 912px;
    height: 372px;
    border-radius: 28px;
    background: linear-gradient(100deg, var(--metal-light) 0%, var(--metal-mid) 45%, var(--metal-light) 70%, var(--metal-dark) 100%);
    font-family: "Questrial", "Helvetica Neue", Arial, sans-serif;
    color: var(--ink);
  }
  .brand {
    position: absolute;
    left: 40px;
    top: 160px;
    display: flex;
    align-items: center;
    gap: 12px;
  }
  .brand-dot {
    width: 28px;
    height: 28px;
    border-radius: 50%;
    background: var(--ink);
  }
  .brand-name {
    font-size: 30px;
    line-height: 1;
    white-space: nowrap;
  }
  .wearer {
    position: absolute;
    right: 36px;
    top: 128px;
    text-align: right;
  }
  .wearer-name {
    font-size: 60px;
    line-height: 1.05;
    font-weight: 400;
  }
  .wearer-title {
    font-size: 40px;
    line-height: 1.2;
  }
</style>
</head>
<body>
  <main class="canvas">
    <section class="name-tag">
      <div class="brand">
        <span class="brand-dot"></span>
        <span class="brand-name">Palm Rest Care</span>
      </div>
      <div class="wearer">
        <h1 class="wearer-name">Miriam Dorsey</h1>
        <p class="wearer-title">Certified Hand Therapist</p>
      </div>
    </section>
  </main>
</body>
</html>
```